Nexor Turbo Business Card Design

This is a start up company that has state of the art patented technology for turbo chargers,that can be used on engines, gas or diesel, for any type of automotive,aviation,marine or industrial purpose.
This technology will provide longer life,lower maintenance and better performance and help produce lower emissions with any turbocharged engine.Red would be a predominate color and the design should communicate the latest technology,economy and
Environmental concern.
This product will initially be distributed in the U.S.A. But should move rapidly to global use.
Updates

Thank you for your design submissions, I have increased the budget for this job because my initial order was too low for the quality of work shown, plus I would Like to see some more options. I have a meeting this Sunday with my other partners and would anticipate being able to give you some feedback by the Beginning of next week. Regards.

Thank you for everyone's participation. The deadline is still open until 6/15 and my partners and I have a meeting Scheduled this weekend. At this time we have not ruled anyone out, But will be making a decision during the course of our meeting and wil Decide which direction we will be going in by the beginning of the week. Thanks again, regards, Dan Ferris.

Hello everybody, Sorry for the delay in communication, we have been very busy in putting the start up together. We are still not decided on the design of the business card and have a wide range to choose from. I would anticipated we shall have an answer within the next two weeks. Regards, Dan Ferris.

Target Market(s)

Manufacturers and wholesalers' of OEM and replacement turbochargers

Industry/Entity Type

Industrial

Contact Information for Business Card

We need a logo that should incorporate the " Nexor, a " possibly super imposed over a turbo charger with the fan blades of the turbocharger showing in the center of the "a" .
Name,title,phone number and email address only, no street/mailing address at this time.
The full name of the company is
" Nexor Turbo Technologies LLC "
For the initial card you can use my info.
Daniel Ferris
VP Sales & Marketing
dferris@nexorturbotechnologies.com
555 014 2876

Requirements
Must have
• The Nexor A, the outline of a turbo charger
Nice to have
• Something classy and simple and worldly (global)
Should not have
• No engines,cars,boats,planes

```html
<!DOCTYPE html>
<html lang="en">
<head>
<meta charset="utf-8">
<title>Nexor Turbo Technologies – Business Card</title>
<link rel="stylesheet" href="https://fonts.googleapis.com/css2?family=Open+Sans:wght@400;600;700&display=swap">
<style>
  :root {
    --stage: #3b1010;
    --card: #ffffff;
    --accent: #f26a1b;
    --ink: #141414;
    --band: #0d0d0d;
    --mark-faint: #efe9e4;
  }
  * { margin: 0; padding: 0; box-sizing: border-box; }
  html, body {
    width: 1200px;
    height: 800px;
    overflow: hidden;
    background: var(--stage);
    font-family: "Open Sans", Arial, sans-serif;
  }
  .business-card {
    position: absolute;
    left: 75px;
    top: 100px;
    width: 1050px;
    height: 600px;
    background: var(--card);
    overflow: hidden;
    box-shadow: 0 20px 40px rgba(0,0,0,0.45);
  }
  .brand {
    position: absolute;
    left: 70px;
    top: 110px;
    display: flex;
    align-items: center;
    gap: 26px;
  }
  .brand-dot {
    width: 120px;
    height: 120px;
    border-radius: 50%;
    background: var(--accent);
    flex: none;
  }
  .brand-name {
    color: var(--accent);
    font-weight: 600;
    font-size: 42px;
    line-height: 1.1;
    letter-spacing: 2px;
    text-transform: uppercase;
  }
  .backdrop-circle {
    position: absolute;
    right: 40px;
    top: 40px;
    width: 280px;
    height: 280px;
    border-radius: 50%;
    background: var(--mark-faint);
  }
  .contact {
    position: absolute;
    left: 70px;
    top: 295px;
    color: var(--ink);
  }
  .contact-name {
    color: var(--accent);
    font-weight: 700;
    font-size: 34px;
    line-height: 1.1;
  }
  .contact-title {
    font-size: 20px;
    margin-top: 2px;
  }
  .contact-list {
    list-style: none;
    margin-top: 22px;
  }
  .contact-item {
    display: flex;
    align-items: center;
    gap: 14px;
    font-size: 27px;
    line-height: 1.45;
  }
  .contact-icon { width: 26px; height: 26px; flex: none; }
  .accent-line {
    position: absolute;
    left: 0;
    right: 0;
    top: 472px;
    height: 7px;
    background: var(--accent);
  }
  .base-band {
    position: absolute;
    left: 0;
    right: 0;
    top: 479px;
    bottom: 0;
    background: var(--band);
  }
</style>
</head>
<body>
  <div class="business-card">
    <div class="backdrop-circle" aria-hidden="true"></div>

    <div class="brand">
      <div class="brand-dot" aria-hidden="true"></div>
      <div class="brand-name">Nexor Turbo<br>Technologies</div>
    </div>

    <div class="contact">
      <div class="contact-name">Daniel Ferris</div>
      <div class="contact-title">VP Sales &amp; Marketing</div>
      <ul class="contact-list">
        <li class="contact-item">
          <svg class="contact-icon" viewBox="0 0 24 24" aria-hidden="true">
            <path fill="#f26a1b" d="M6.6 10.8a15.1 15.1 0 0 0 6.6 6.6l2.2-2.2c.3-.3.7-.4 1-.2 1.1.4 2.3.6 3.6.6.6 0 1 .4 1 1V20c0 .6-.4 1-1 1A17 17 0 0 1 3 4c0-.6.4-1 1-1h3.5c.6 0 1 .4 1 1 0 1.3.2 2.5.6 3.6.1.3 0 .7-.2 1z"/>
          </svg>
          <span>555 014 2876</span>
        </li>
        <li class="contact-item">
          <svg class="contact-icon" viewBox="0 0 24 24" aria-hidden="true">
            <path fill="#f26a1b" d="M2 9l10-7 10 7v12H2z"/>
            <path fill="#ffffff" d="M4 10l8 5 8-5v2l-8 5-8-5z"/>
          </svg>
          <span>dferris@nexorturbotechnologies.com</span>
        </li>
      </ul>
    </div>

    <div class="accent-line"></div>
    <div class="base-band"></div>
  </div>
</body>
</html>
```